Tech Savy small Business accountant business card design

We need a business card for a new company based in the cloud. We provide tax, business advisory, accounting, information technology solutions and back office functions to small businesses. We offer fixed fee packages with add on services as you need them. By harnessing technology we simplify small business operational processes providing valuable time and information for small business owners to grow their business. In the logo (zulvarine) we want to be able to see zulv and experts. The final design should communicate achieving growth dreams and balance (ie life and $).
Updates
This project has been temporarily placed on hold until I finalize "Tech Savy small Business accountant needs a logo". I invite all designers to submit on this logo project. Once my logo is finalized I will resume this business card contest. Thanks Added Wednesday, March 19, 2014
This project has been temporarily placed on hold until I finalize "Tech Savy small Business accountant logo". I invite all designers to submit on this logo project. Once my logo is finalized I will resume this business card contest. Thanks Added Thursday, March 20, 2014
Target Market(s)
Small Business (Revenue $500,000, more than 3 employees) owners.
Industry/Entity Type
Small Business
Contact Information for Business Card
Marla Pennick (Principal)
Accountant, Tax Agent.
TEL | 0417 583 916
EMAIL | Marla.Pennick@zulvarine.com.au
WEB | www.zulvarine.com.au
Look and feel

```html
<!DOCTYPE html>
<html lang="en">
<head>
<meta charset="utf-8">
<title>Zulvarine Business Card</title>
<link rel="stylesheet" href="https://fonts.googleapis.com/css2?family=Exo+2:wght@400;500;600;700&display=swap">
<style>
  :root {
    --backdrop: #2e2e30;
    --card-frame: #3d3d3f;
    --tile-grey: #4e4e50;
    --band-grey: #5a5a5c;
    --band-light: #e9e9ea;
    --ink-dark: #4a4a4c;
    --ink-light: #ffffff;
    --accent-pink: #e0529a;
    --accent-blue: #27a3dc;
    --accent-green: #8cc63f;
  }
  * { box-sizing: border-box; margin: 0; padding: 0; }
  html, body {
    width: 1200px; height: 1200px; overflow: hidden;
    background: var(--backdrop);
    font-family: "Exo 2", sans-serif;
  }
  .canvas {
    width: 1200px; height: 1200px;
    display: flex; flex-direction: column;
    align-items: center; justify-content: center; gap: 66px;
  }
  .card {
    width: 900px; height: 500px;
    background: var(--card-frame);
    box-shadow: 0 10px 30px rgba(0,0,0,.35);
    position: relative;
  }

  /* Back side */
  .card-back {
    padding: 24px;
    display: grid;
    grid-template-rows: 96px 1fr 96px;
    gap: 12px;
  }
  .band { background: var(--band-grey); }
  .band-feature {
    background: var(--band-light);
    display: flex; flex-direction: column; justify-content: center;
    padding-left: 150px;
  }
  .brand-name {
    font-weight: 700; font-size: 86px; line-height: 1;
    letter-spacing: -1px; color: var(--ink-dark);
  }
  .band-feature .tagline {
    font-size: 24px; color: var(--ink-dark); margin-top: 4px; padding-left: 10px;
  }

  /* Front side */
  .card-front {
    padding: 24px;
    display: grid;
    grid-template-columns: 364px 232px 232px;
    grid-template-rows: 220px 220px;
    gap: 12px;
  }
  .tile {
    position: relative;
    background: var(--tile-grey);
    color: var(--ink-light);
    padding: 18px 20px;
  }
  .tile-pink { background: var(--accent-pink); }
  .tile-blue { background: var(--accent-blue); }
  .tile-green { background: var(--accent-green); }
  .tile .icon {
    position: absolute; top: 22px; right: 22px;
    width: 40px; height: 40px;
  }
  .tile-brand { display: flex; flex-direction: column; justify-content: center; padding-left: 24px; }
  .tile-brand .brand-name { color: var(--ink-light); font-size: 66px; }
  .tile-brand .tagline { font-size: 17px; margin-top: 4px; padding-left: 4px; }

  .tile-name { text-align: right; display: flex; flex-direction: column; justify-content: flex-end; }
  .person-first { font-weight: 700; font-size: 46px; line-height: 1; }
  .person-last { font-weight: 400; font-size: 38px; line-height: 1.05; }
  .person-role { font-size: 17px; font-weight: 500; margin-top: 8px; }

  .tile-title { text-align: right; display: flex; align-items: flex-end; justify-content: flex-end;
    font-size: 18px; font-weight: 500; line-height: 1.3; }

  .tile-web { text-align: right; display: flex; flex-direction: column; justify-content: flex-end; }
  .web-prefix { font-size: 56px; font-weight: 400; letter-spacing: 6px; line-height: 1; }
  .web-domain { font-size: 18px; letter-spacing: 1px; }

  .tile-email { display: flex; flex-direction: column; justify-content: flex-end;
    font-size: 17px; font-weight: 500; line-height: 1.3; }
  .email-user { font-size: 21px; }

  .tile-phone { display: flex; align-items: flex-end; font-size: 22px; font-weight: 500; letter-spacing: 1px; }
</style>
</head>
<body>
<main class="canvas">

  <section class="card card-back" aria-label="Business card back">
    <div class="band"></div>
    <div class="band-feature">
      <div class="brand-name">zulvarine</div>
      <div class="tagline">Your business and accounting partner</div>
    </div>
    <div class="band"></div>
  </section>

  <section class="card card-front" aria-label="Business card front">
    <div class="tile tile-brand">
      <div class="brand-name">zulvarine</div>
      <div class="tagline">Your business and accounting partner</div>
    </div>

    <div class="tile tile-blue tile-name">
      <svg class="icon" viewBox="0 0 40 40" aria-hidden="true">
        <circle cx="20" cy="13" r="8" fill="#fff"/>
        <path d="M5 38 C5 26 35 26 35 38 Z" fill="#fff"/>
      </svg>
      <div class="person-first">MARLA</div>
      <div class="person-last">PENNICK</div>
      <div class="person-role">PRINCIPAL</div>
    </div>

    <div class="tile tile-title">
      <svg class="icon" viewBox="0 0 40 40" aria-hidden="true">
        <path d="M8 32 L12 22 L28 6 L34 12 L18 28 Z" fill="none" stroke="#fff" stroke-width="2.5" stroke-linejoin="round"/>
        <path d="M12 22 L18 28" stroke="#fff" stroke-width="2.5"/>
      </svg>
      <div>ACCOUNTANT &amp;<br>TAX AGENT</div>
    </div>

    <div class="tile tile-pink tile-web">
      <svg class="icon" viewBox="0 0 40 40" aria-hidden="true">
        <rect x="3" y="5" width="34" height="23" fill="none" stroke="#fff" stroke-width="3"/>
        <rect x="17" y="28" width="6" height="5" fill="#fff"/>
        <rect x="11" y="33" width="18" height="3" fill="#fff"/>
      </svg>
      <div class="web-prefix">WWW</div>
      <div class="web-domain">.ZULVARINE.COM.AU</div>
    </div>

    <div class="tile tile-email">
      <svg class="icon" viewBox="0 0 40 40" aria-hidden="true">
        <rect x="3" y="8" width="34" height="24" fill="#fff"/>
        <path d="M3 8 L20 22 L37 8" fill="none" stroke="#4e4e50" stroke-width="2"/>
      </svg>
      <div class="email-user">MARLA.PENNICK</div>
      <div>@ZULVARINE.COM.AU</div>
    </div>

    <div class="tile tile-green tile-phone">
      <svg class="icon" viewBox="0 0 40 40" aria-hidden="true">
        <path d="M4 14 C4 6 36 6 36 14 L30 16 L28 12 L12 12 L10 16 Z" fill="#fff"/>
        <path d="M12 16 L28 16 L33 34 L7 34 Z" fill="#fff"/>
        <circle cx="20" cy="25" r="4" fill="#8cc63f"/>
      </svg>
      <div>0417 583 916</div>
    </div>
  </section>

</main>
</body>
</html>
```